" atendimento de pacientes de ambos os gêneros com uma ênfase em mulheres, oferecemos cirurgia plástica estética e reparadora . local de requinte e sofisticação "

```html
<!DOCTYPE html>
<html lang="pt-BR">
<head>
<meta charset="UTF-8">
<title>Serena Lumi – Cirurgia Plástica</title>
<link href="https://fonts.googleapis.com/css2?family=Montserrat:wght@400;500&display=swap" rel="stylesheet">
<style>
  :root {
    --backdrop: #e8e4de;
    --plate: #0b0b0b;
    --plate-edge: #1c1c1c;
    --gold-light: #f3c15a;
    --gold: #d99a2b;
    --gold-deep: #a86d12;
    --ink-light: #f2f2f2;
  }
  * { margin: 0; padding: 0; box-sizing: border-box; }
  html, body {
    width: 1200px;
    height: 1200px;
    overflow: hidden;
    background: var(--backdrop);
  }
  .stage {
    width: 1200px;
    height: 1200px;
    display: flex;
    align-items: center;
    justify-content: center;
  }
  .sign {
    position: relative;
    width: 960px;
    height: 740px;
    background: var(--plate);
    border: 4px solid var(--plate-edge);
    border-radius: 70px;
  }
  .sign-frame {
    position: absolute;
    inset: 30px;
    border-radius: 48px;
    border: 10px solid var(--gold);
    border-color: var(--gold-light) var(--gold) var(--gold-deep) var(--gold);
  }
  .brand {
    position: absolute;
    left: 0;
    right: 0;
    top: 290px;
    display: flex;
    flex-direction: column;
    align-items: center;
    gap: 22px;
  }
  .brand-name {
    display: flex;
    align-items: center;
    gap: 22px;
    font-family: "Montserrat", sans-serif;
    font-weight: 500;
    font-size: 84px;
    line-height: 1;
    letter-spacing: 1px;
    color: var(--gold);
  }
  .brand-dot {
    width: 26px;
    height: 26px;
    border-radius: 50%;
    background: var(--gold);
  }
  .brand-tagline {
    font-family: "Montserrat", sans-serif;
    font-weight: 400;
    font-size: 26px;
    letter-spacing: 3px;
    color: var(--ink-light);
  }
  .contact-row {
    position: absolute;
    left: 0;
    right: 0;
    top: 590px;
    display: flex;
    align-items: center;
    justify-content: center;
    gap: 22px;
    font-family: "Montserrat", sans-serif;
    font-weight: 500;
    font-size: 26px;
    color: var(--ink-light);
  }
  .contact-item {
    display: flex;
    align-items: center;
    gap: 14px;
  }
  .contact-icon {
    width: 28px;
    height: 28px;
    fill: var(--ink-light);
  }
  .contact-divider {
    width: 3px;
    height: 32px;
    background: var(--ink-light);
    margin: 0 24px;
  }
</style>
</head>
<body>
  <main class="stage">
    <section class="sign">
      <div class="sign-frame"></div>

      <header class="brand">
        <h1 class="brand-name"><span class="brand-dot" aria-hidden="true"></span>Serena Lumi</h1>
        <p class="brand-tagline">Cirúrgia Plástica</p>
      </header>

      <footer class="contact-row">
        <div class="contact-item">
          <svg class="contact-icon" viewBox="0 0 24 24" aria-hidden="true">
            <path d="M6.6 10.8a15.1 15.1 0 0 0 6.6 6.6l2.2-2.2a1 1 0 0 1 1-.25 11.4 11.4 0 0 0 3.6.57 1 1 0 0 1 1 1V20a1 1 0 0 1-1 1A17 17 0 0 1 3 4a1 1 0 0 1 1-1h3.5a1 1 0 0 1 1 1c0 1.25.2 2.45.57 3.57a1 1 0 0 1-.25 1z"/>
          </svg>
          <span>(000) 0000-0000</span>
        </div>
        <span class="contact-divider"></span>
        <div class="contact-item">
          <svg class="contact-icon" viewBox="0 0 24 24" aria-hidden="true">
            <path d="M12 2a7 7 0 0 0-7 7c0 5.25 7 13 7 13s7-7.75 7-13a7 7 0 0 0-7-7zm0 9.5A2.5 2.5 0 1 1 12 6.5a2.5 2.5 0 0 1 0 5z"/>
          </svg>
          <span>Rua Flores, Centro 120</span>
        </div>
      </footer>
    </section>
  </main>
</body>
</html>
```